Garage Door Company seeking business card designs.
Harbor Ridge Door
Professional
Miles Tandry
Owner, Operator.
We don't want a address listed...
Miles@HarborRidgeDoor.com
www.PortalLiftExperts.com
We want to publish three numbers: Alder Falls - 320.555.0147 Pine Hollow - 320.555.0192 Cedar Bend - 952.555.0163 on front... Commercial and Residential On back... New Garage Door Sales and Installation. Repair and Maintenance Services. List website; www.PortalLiftExperts.com Have name, title, phone numbers, email, and website on one side. Motto's and verbiage on the other back side. Logo likely on front very prominently. Front can be full color, and back should be back letter, or the door of the logo lettering.
"When it won't lift, we make it rise!" Sales and Installation. Repair and Maintenance.

```html
<!DOCTYPE html>
<html lang="en">
<head>
<meta charset="utf-8">
<title>Harbor Ridge Door — Business Card</title>
<link rel="stylesheet" href="https://fonts.googleapis.com/css2?family=Oswald:wght@300;400;600&display=swap">
<style>
  :root {
    --backdrop: #8c8c8c;
    --forest: #4a5d28;
    --forest-deep: #3e4f21;
    --paper: #ffffff;
    --ink: #3b4a20;
    --ink-soft: #55633a;
  }
  * { box-sizing: border-box; margin: 0; padding: 0; }
  html, body {
    width: 1200px; height: 876px; overflow: hidden;
    background: var(--backdrop);
    font-family: "Oswald", "Arial Narrow", sans-serif;
  }
  .stage {
    position: relative; width: 1200px; height: 876px;
    display: flex; align-items: center; justify-content: center; gap: 40px;
  }
  .card {
    position: relative; width: 540px; height: 309px;
    box-shadow: 0 10px 24px rgba(0,0,0,.28);
    overflow: hidden;
  }

  /* Front side */
  .card--front { background: var(--paper); color: var(--ink); }
  .contact { position: absolute; left: 30px; top: 22px; }
  .contact__name { font-size: 22px; font-weight: 400; letter-spacing: .5px; line-height: 1.3; }
  .contact__title { font-size: 11px; font-weight: 300; margin-bottom: 8px; color: var(--ink-soft); }
  .contact__line { font-size: 11.5px; font-weight: 400; line-height: 1.45; }
  .offices {
    position: absolute; left: 30px; top: 170px;
    display: flex; gap: 28px;
  }
  .office__town { font-size: 12px; font-weight: 600; line-height: 1.4; }
  .office__phone { font-size: 11.5px; font-weight: 400; line-height: 1.4; }
  .brand--front {
    position: absolute; right: 28px; top: 120px;
    display: flex; align-items: center; gap: 10px;
  }
  .brand__mark { width: 22px; height: 22px; background: var(--forest); flex: none; }
  .brand__name {
    font-size: 28px; font-weight: 600; letter-spacing: 1px;
    text-transform: uppercase; color: var(--forest); line-height: 1;
    white-space: nowrap;
  }
  .band {
    position: absolute; left: 0; right: 0; bottom: 0; height: 80px;
    background: var(--forest);
    display: flex; align-items: center; padding-left: 30px;
  }
  .band__text {
    color: var(--paper); font-size: 16px; font-weight: 400;
    letter-spacing: 2px; text-transform: uppercase;
  }

  /* Back side */
  .card--back {
    background: linear-gradient(160deg, var(--forest) 0%, var(--forest-deep) 100%);
    color: var(--paper);
  }
  .motto { position: absolute; left: 30px; top: 26px; text-transform: uppercase; }
  .motto__quote { font-size: 15px; font-weight: 400; letter-spacing: 1px; margin-bottom: 6px; }
  .motto__service { font-size: 11px; font-weight: 300; letter-spacing: 1px; line-height: 1.5; }
  .brand--back {
    position: absolute; right: 34px; top: 150px;
    display: flex; flex-direction: column; align-items: flex-end;
  }
  .brand--back .brand__row { display: flex; align-items: center; gap: 10px; }
  .brand--back .brand__mark { background: var(--paper); }
  .brand--back .brand__name { color: var(--paper); font-size: 34px; }
  .brand__web { margin-top: 10px; font-size: 12px; font-weight: 300; letter-spacing: 1px; }
</style>
</head>
<body>
<main class="stage">
  <section class="card card--front" aria-label="Business card front">
    <div class="contact">
      <p class="contact__name">Miles Tandry</p>
      <p class="contact__title">Owner, Operator</p>
      <p class="contact__line">320.555.0147</p>
      <p class="contact__line">Miles@HarborRidgeDoor.com</p>
      <p class="contact__line">www.PortalLiftExperts.com</p>
    </div>
    <div class="brand brand--front">
      <span class="brand__mark"></span>
      <span class="brand__name">Harbor Ridge Door</span>
    </div>
    <div class="offices">
      <div class="office"><p class="office__town">Alder Falls</p><p class="office__phone">320.555.0147</p></div>
      <div class="office"><p class="office__town">Pine Hollow</p><p class="office__phone">320.555.0192</p></div>
      <div class="office"><p class="office__town">Cedar Bend</p><p class="office__phone">952.555.0163</p></div>
    </div>
    <div class="band"><p class="band__text">Commercial and Residential</p></div>
  </section>

  <section class="card card--back" aria-label="Business card back">
    <div class="motto">
      <p class="motto__quote">“When it won’t lift, we make it rise!”</p>
      <p class="motto__service">Sales and Installation</p>
      <p class="motto__service">Repair and Maintenance</p>
    </div>
    <div class="brand brand--back">
      <div class="brand__row">
        <span class="brand__mark"></span>
        <span class="brand__name">Harbor Ridge Door</span>
      </div>
      <p class="brand__web">www.PortalLiftExperts.com</p>
    </div>
  </section>
</main>
</body>
</html>
```